Stationery Design Project for Velmora, Chicago

Velmora, a street parking application which helps car drivers find a street parking spot by offering an ideal path along which to look for parking. This path is calculated by our algorithm based on data (e.g. historical data, baseball games schedule, etc.). Along this path the driver will find a spot and will also save 70% of the search time. Customer we target is reg. between 21 and 45 yo.

We envision something young, fresh, bright and original. Slightly abstract maybe. It should represent the idea and elements of finding street parking in the city, e.g. car(s), parking spot, people, city, etc. (just ideas!).

Logo is attached.

Requirement:
- Business Cards (2 Sided Full Color CMYK)
- Letterhead (1 Sided Full Color CMYK)
- Envelope (1 Sided Full Color CMYK)
- Sticker (1 Sided Full Color CMYK), round with a 2inch diameter.
Updates

Reason: We're starting to get more and more designs and need more time to look into all of them. Very exciting!! Thanks to everybody!

Hi all, we're in the process of selecting our favs. Though choices!!! Really good submissions. Will keep you posted and sorry for the delay.

Target Market(s)

Car drivers and owners between 21 and 45

Industry/Entity Type

Parking

Requirements
Must have
• Sticker should be round and include company URL velmora.com and the new logo which we will attach soon.
Should not have
• Should not be too serious or boring.

```html
<!DOCTYPE html>
<html lang="en">
<head>
<meta charset="utf-8">
<title>Velmora business card</title>
<link rel="stylesheet" href="https://fonts.googleapis.com/css2?family=Source+Sans+3:wght@400;600;700&display=swap">
<style>
  :root {
    --backdrop: #e9e4de;
    --card: #ffffff;
    --card-edge: #6b6b6b;
    --ink: #3a3a3a;
    --ink-dark: #2b2b2b;
    --divider: #c9c9c9;
    --brand-blue: #1b57c9;
    --brand-blue-deep: #253d93;
    --brand-sky: #2fa3e6;
    --stripe-black: #1f1f1f;
    --photo-top: #6b6058;
    --photo-mid: #4a4a4c;
    --photo-low: #8a8a8c;
  }
  * { box-sizing: border-box; margin: 0; padding: 0; }
  html, body { width: 1200px; height: 1088px; overflow: hidden; }
  body {
    background: var(--backdrop);
    font-family: "Source Sans 3", "Myriad Pro", Arial, sans-serif;
    color: var(--ink);
    position: relative;
  }
  .card {
    position: absolute;
    width: 764px;
    height: 437px;
    background: var(--card);
    border: 1.5px solid var(--card-edge);
    border-radius: 22px;
    overflow: hidden;
  }
  .card--front { left: 90px; top: 73px; }
  .card--back { left: 332px; top: 553px; }

  /* front */
  .brand { position: absolute; left: 153px; top: 39px; display: flex; align-items: center; gap: 26px; }
  .brand__dot {
    width: 128px; height: 128px; border-radius: 50%;
    background: var(--brand-blue);
  }
  .brand__name { font-size: 86px; font-weight: 600; color: var(--ink-dark); letter-spacing: 1px; line-height: 1; }

  .address {
    position: absolute; right: 388px; top: 240px;
    text-align: right; font-size: 19px; line-height: 25px; color: var(--ink);
  }
  .divider { position: absolute; left: 399px; top: 211px; width: 1.5px; height: 116px; background: var(--divider); }
  .contacts { position: absolute; left: 420px; top: 212px; list-style: none; font-size: 19px; line-height: 27px; }
  .contacts li { display: flex; align-items: center; gap: 10px; }
  .contacts svg { width: 15px; height: 15px; fill: var(--ink); flex: none; }

  .band { position: absolute; left: 0; bottom: 0; width: 100%; height: 66px; }
  .signature {
    position: absolute; left: 447px; bottom: 18px;
    color: #fff; font-size: 28px; font-weight: 700; white-space: nowrap;
  }
  .signature__title { font-size: 23px; font-weight: 400; }

  /* back */
  .emblem {
    position: absolute; left: 62px; top: 78px;
    width: 204px; height: 204px; border-radius: 50%;
    background: var(--brand-blue);
    display: flex; align-items: center; justify-content: center;
  }
  .emblem__name { color: #fff; font-size: 38px; font-weight: 600; }
  .web { position: absolute; left: 0; width: 340px; top: 338px; text-align: center; font-size: 20px; letter-spacing: 2.5px; color: var(--ink); }
  .street-photo {
    position: absolute; left: 331px; top: 73px; right: 0; height: 288px;
    background: linear-gradient(180deg, var(--photo-top) 0%, var(--photo-mid) 30%, var(--photo-mid) 70%, var(--photo-low) 100%);
  }
</style>
</head>
<body>
  <section class="card card--front">
    <div class="brand">
      <div class="brand__dot"></div>
      <span class="brand__name">Velmora</span>
    </div>

    <p class="address">Complex Name, Street Name<br>Area, City Name,000 000</p>
    <div class="divider"></div>
    <ul class="contacts">
      <li><svg viewBox="0 0 16 16"><path d="M4 1l3 3-2 2c1 2 3 4 5 5l2-2 3 3-2 3C7 15 1 9 1 3z"/></svg>+91 12345 67890</li>
      <li><svg viewBox="0 0 16 16"><path d="M4 0h8v16H4zM6 2v9h4V2z"/></svg>+91 12345 67890</li>
      <li><svg viewBox="0 0 16 16"><path d="M1 3h14v11H1zM2.5 4.5l5.5 4.5 5.5-4.5z"/></svg>info@velmora.com</li>
      <li><svg viewBox="0 0 16 16"><circle cx="8" cy="8" r="7"/></svg>www.velmora.com</li>
    </ul>

    <svg class="band" viewBox="0 0 764 66" preserveAspectRatio="none" aria-hidden="true">
      <defs>
        <linearGradient id="band-blue" x1="0" x2="1">
          <stop offset="0" stop-color="var(--brand-blue)"/>
          <stop offset="1" stop-color="var(--brand-blue-deep)"/>
        </linearGradient>
      </defs>
      <rect x="0" y="29" width="764" height="37" fill="var(--brand-sky)"/>
      <polygon points="0,3 365,3 348,22 0,22" fill="var(--stripe-black)"/>
      <polygon points="382,0 764,0 764,66 330,66" fill="url(#band-blue)"/>
    </svg>
    <p class="signature">Your Name , <span class="signature__title">Title</span></p>
  </section>

  <section class="card card--back">
    <div class="emblem"><span class="emblem__name">Velmora</span></div>
    <p class="web">www.velmora.com</p>
    <div class="street-photo" role="img" aria-label="Photo of a city street from above with cars parked along both curbs"></div>
  </section>
</body>
</html>
```